Album art design concept, my band will be releasing a 11 song rock album in the next few Months. We will be using it as a CD cover, poster, online art cover, maybe even Vinyl. Working album titles are "Woven from static" (Preferred album title) or "The river under the stone". Anything abstract, painting-like design, or whatever type of design that comes to mind. Fonts are designers choice. Thank You

Target Market(s)

Music business

Colors

Designer to choose colors to be used in the design.

Requirements
Must have
• Our band logo
Nice to have
• Anything abstract, attractive painting type, maybe even some kind of a futuristic design.
Should not have
• Skulls, blood-like, scary designs, nudity, emo type of design

```html
<!DOCTYPE html>
<html lang="en">
<head>
<meta charset="utf-8">
<title>Lantern Hollow — Woven from Static</title>
<link rel="stylesheet" href="https://fonts.googleapis.com/css2?family=Exo+2:wght@200;600&display=swap">
<style>
  :root {
    --backdrop: #d3d5d2;
    --ink-light: #f4f2ee;
    --accent-red: #d8252a;
    --paint-yellow: #d9cf6a;
    --paint-green: #5f8a2a;
    --paint-orange: #c8521a;
    --paint-red: #8e1410;
    --paint-blue: #1d2f9a;
    --paint-teal: #1f9bb0;
    --paint-black: #0b0807;
  }
  * { margin: 0; padding: 0; box-sizing: border-box; }
  html, body {
    width: 1200px;
    height: 850px;
    overflow: hidden;
    background: var(--backdrop);
  }
  .canvas {
    position: relative;
    width: 1200px;
    height: 850px;
    display: flex;
    align-items: center;
    justify-content: center;
  }
  .album-cover {
    position: relative;
    width: 780px;
    height: 780px;
    overflow: hidden;
    background: var(--paint-black);
  }
  .cover-artwork {
    position: absolute;
    inset: 0;
    background:
      radial-gradient(ellipse 45% 40% at 20% 28%, rgba(217,207,106,0.95), transparent 70%),
      radial-gradient(ellipse 40% 45% at 12% 60%, rgba(95,138,42,0.9), transparent 70%),
      radial-gradient(ellipse 35% 30% at 8% 92%, rgba(40,120,40,0.85), transparent 70%),
      radial-gradient(ellipse 45% 40% at 70% 22%, rgba(200,82,26,0.85), transparent 70%),
      radial-gradient(ellipse 45% 40% at 60% 55%, rgba(142,20,16,0.95), transparent 70%),
      radial-gradient(ellipse 60% 14% at 75% 80%, rgba(29,47,154,0.95), transparent 75%),
      radial-gradient(ellipse 30% 18% at 90% 94%, rgba(31,155,176,0.9), transparent 70%),
      linear-gradient(180deg, #6e5a16 0%, #7a2410 55%, var(--paint-black) 100%);
  }
  .band-name {
    position: absolute;
    top: 72px;
    right: 152px;
    font-family: "Exo 2", sans-serif;
    font-weight: 600;
    font-size: 60px;
    line-height: 0.98;
    letter-spacing: 1px;
    text-transform: uppercase;
    text-align: right;
    color: var(--ink-light);
  }
  .album-title {
    position: absolute;
    left: 0;
    right: 0;
    bottom: 26px;
    font-family: "Exo 2", sans-serif;
    font-weight: 200;
    font-size: 50px;
    letter-spacing: 1px;
    text-transform: uppercase;
    text-align: center;
    color: var(--ink-light);
  }
  .album-title .title-accent { color: var(--accent-red); }
</style>
</head>
<body>
  <main class="canvas">
    <section class="album-cover">
      <div class="cover-artwork" role="img" aria-label="Abstract painted collage in yellow, green, red and blue with a faint standing figure"></div>
      <h1 class="band-name">Lantern<br>Hollow</h1>
      <h2 class="album-title">Woven <span class="title-accent">from</span> Static</h2>
    </section>
  </main>
</body>
</html>
```